eMira7: Web Landing / Homepage (Design Only / Logo Supplied!)

Landing / Homepage
(Design Only / Logo Supplied!)

eMira7 should be just what it looks like as in a resemblance of the logo for Vorto qBolt.

The real logo aspect should be the adaptation of the universal symbol for infinity incorporated with a directional arrow indicating infinite motion.

This should be incorporated with the eMira7/Infinity Sign

- Overview / Background of the Business

Recently I was bullied out of a job and it ruined my life, temporarily. Everything was taken from me, my self esteem, my finances, my emotional and physical health. I decided to start a diversity and social sustainability consulting firm.

The primary goal of my business is to promote ethnic/social/cultural diversity and equality in the workplace. I am going to do public speaking engagements and consulting with companies on how to develop more inclusive policies in the workplace.

- The Target Market / Audience we are trying to reach

My target market is those who would align themselves with social/economic progressives, Harbor Tent Rising sympathisers and others who value political and economic equality and would like to change issues such as economic, gender, racial, and class equality issues.

- Design Specifics; preferences or ideas for Style, Colour, Font, Imagery, etc

Only Black, Grey, or Dark Blue. Please see the attachment for the infinity sign for ideas of where to start the design and incorporate it in with

- Content to be included in the web design

We require a Homepage
The content will be structured as a interactive website for news, information, and support for people who have been marginalised, bullied, oppressed, and harassed and want to positively contribute back into society, instead of hurting themselves or others.

Target Market(s)

18-45 year old Bullying and Discrimination victims and those who are sensitive to those with mental health issues.

Industry/Entity Type

Sustainability

Requirements
Must have
• eMira7 and the infinity sign must be elegantly and smoothly integrated

It should focus on the colours black, blue, grey and be professional in look and feel.

Navigation and tone should be serious and feel like a news paper or serious news magazine outlook
Nice to have
• Rollovers leading to other sites about bullying, discrimination, gender bias and age discrimination.

The site should be as cross platform as possible.
Should not have
• Unknown at this time

```html
<!DOCTYPE html>
<html lang="en">
<head>
<meta charset="utf-8">
<title>eMira7 — Social Justice, Sustainability, Inclusion</title>
<link href="https://fonts.googleapis.com/css2?family=Source+Sans+3:wght@400;600;700&family=Oswald:wght@500&display=swap" rel="stylesheet">
<style>
:root{
  --ink:#1e1e1e;
  --text:#3a3a3a;
  --muted:#7a7a7a;
  --rule:#dcdcdc;
  --panel:#efefef;
  --nav-top:#5a5a5a;
  --nav-bot:#2e2e2e;
  --frame:#3d3d3d;
  --accent:#c0392b;
  --bg:#ffffff;
  --header-bg:#f7f8fa;
}
*{box-sizing:border-box;margin:0;padding:0}
html,body{width:769px;height:1200px;overflow:hidden;background:var(--bg)}
body{position:relative;font-family:"Source Sans 3",Arial,sans-serif;color:var(--text)}
.abs{position:absolute}
.top-strip{left:0;top:0;width:769px;height:3px;background:#333}
.header{left:0;top:3px;width:769px;height:116px;background:var(--header-bg);border-bottom:1px solid #e6e6e6}
.brand{left:28px;top:8px;width:134px;height:92px;background:#f1f2f4;display:flex;flex-direction:column;align-items:center;justify-content:center;gap:6px}
.brand-mark{width:30px;height:30px;border-radius:50%;background:var(--ink)}
.brand-name{font-size:22px;font-weight:600;color:var(--ink);letter-spacing:1px}
.brand-tag{font-size:6px;letter-spacing:2px;color:var(--text);text-align:center;line-height:7px;margin-top:-4px}
.social{top:40px;left:663px;display:flex;gap:2px}
.social span{width:18px;height:18px;border-radius:50%;background:#2b2b2b}
.search{left:558px;top:68px;width:182px;height:21px;background:#ececec;border:1px solid #e0e0e0;font-size:9px;color:#555;padding:4px 9px}
.search svg{position:absolute;right:9px;top:6px}
.nav{left:25px;top:102px;width:718px;height:35px;border-radius:3px;background:linear-gradient(var(--nav-top),var(--nav-bot));display:flex;align-items:center;justify-content:space-around;padding:0 20px}
.nav a{color:#f1f1f1;font-size:11px;text-decoration:none}
.nav i{width:1px;height:14px;background:#777}
.slider{left:25px;top:140px;width:720px;height:264px;background:var(--frame);border-radius:3px}
.slide-photo{left:14px;top:11px;width:496px;height:234px;background:linear-gradient(90deg,#3a4fa8 0%,#dfe6f3 18%,#5a5c66 40%,#1b1b1f 70%,#0e0e10 100%)}
.slide-copy{left:510px;top:11px;width:195px;height:234px;background:#060606;padding:17px 19px;color:#fff}
.slide-copy h2{font-size:15px;font-weight:400;margin-bottom:7px}
.slide-copy .lead{font-size:9.5px;line-height:14px;margin-bottom:9px}
.slide-copy .body{font-size:7.8px;line-height:14px;color:#ddd}
.slide-btn{display:inline-block;margin-top:9px;margin-left:-3px;background:#2c2c2c;border-radius:3px;padding:5px 11px;font-family:"Oswald",sans-serif;font-size:8px;color:#fff}
.dots{display:flex;gap:3px}
.dots span{width:5px;height:5px;border-radius:50%;background:#fff}
.dots.under span{background:#777;width:6px;height:6px}
.hr{height:1px;background:var(--rule)}
.section-title{font-size:16px;font-weight:400;color:var(--ink)}
.card{width:160px}
.card .thumb{height:113px;border:1px solid #ddd}
.card h3{font-size:10px;font-weight:400;color:var(--ink);margin:10px 2px 4px}
.card p{font-size:8px;line-height:14px;color:var(--muted);text-align:justify;margin:0 2px}
.welcome{left:33px;top:692px;width:480px}
.welcome h2{font-size:16px;font-weight:400;color:var(--ink);margin-bottom:7px}
.welcome .intro{font-size:8px;line-height:14px;color:var(--ink);margin-bottom:9px}
.welcome p{font-size:8px;line-height:14px;color:var(--muted);text-align:justify}
.side-band{background:linear-gradient(90deg,#f5f5f5,#e7e7e7);border-left:1px solid var(--rule);padding:10px 14px;font-size:13px;color:var(--ink)}
.video{left:546px;top:720px;width:201px;height:146px;background:linear-gradient(160deg,#2a4a82,#7fa2d4 55%,#4d5a6c)}
.play{position:absolute;left:82px;top:53px}
.vrule{left:534px;top:676px;width:1px;height:454px;background:var(--rule)}
.box{width:235px}
.box h3{background:linear-gradient(90deg,#ececec,#f6f6f6);font-size:11px;font-weight:400;color:var(--ink);padding:10px 13px;line-height:14px}
.box p{font-size:8px;line-height:14px;color:var(--muted);text-align:justify;margin:10px 3px 0}
.learn{font-family:"Oswald",sans-serif;font-size:8.5px;color:var(--ink);margin:14px 3px 0;display:block}
.post{left:549px;width:197px;display:flex;gap:9px}
.post .pic{width:50px;height:50px;flex:none}
.post h4{font-size:7.6px;font-weight:600;color:var(--ink);margin-bottom:3px}
.post p{font-size:7.4px;line-height:12.7px;color:var(--muted);text-align:justify}
.post a{font-size:7.4px;color:var(--accent);text-decoration:none}
.footer{left:0;top:1165px;width:769px;height:35px;background:#f0f0f0;font-size:7.5px;color:#444;display:flex;justify-content:space-between;align-items:center;padding:0 31px}
</style>
</head>
<body>
<div class="abs top-strip"></div>
<header class="abs header">
  <div class="abs brand">
    <span class="brand-mark"></span>
    <span class="brand-name">eMira7</span>
    <span class="brand-tag">social justice<br>social sustainability<br>social inclusion</span>
  </div>
  <div class="abs social"><span></span><span></span><span></span><span></span></div>
  <div class="abs search">Search here..
    <svg width="4" height="7" viewBox="0 0 4 7"><path d="M0 0L4 3.5 0 7z" fill="#333"/></svg>
  </div>
</header>

<nav class="abs nav">
  <a href="#">Main</a><i></i><a href="#">About Us</a><i></i><a href="#">Latest News</a><i></i><a href="#">Recent Blog</a><i></i><a href="#">Testimonials</a><i></i><a href="#">Projects</a><i></i><a href="#">Services</a><i></i><a href="#">FAQ</a><i></i><a href="#">Contact Us</a>
</nav>

<section class="abs slider">
  <div class="abs slide-photo" role="img" aria-label="Photo of a smiling speaker in a dark suit on stage"></div>
  <div class="abs slide-copy">
    <h2>Recent Headline here</h2>
    <p class="lead">Mauris vel lacus vitae felis vestibu-lum volutpat. Etiam est nunc, venenatis in, tristique eu.</p>
    <p class="body">Cum sociis natoque penatibus et magnis dis parturient montes, nascetur ridiculus mus. In iaculis facilisis massa. Etiam eu urna. Sed porta. Suspendisse quam leo, molestie sed, luctus quis, feugiat in</p>
    <span class="slide-btn">LEARN MORE</span>
    <div class="dots" style="margin-top:14px;margin-left:3px"><span></span><span></span><span></span><span></span></div>
  </div>
</section>
<div class="abs dots under" style="left:369px;top:412px"><span></span><span></span><span></span><span></span></div>
<div class="abs hr" style="left:0;top:428px;width:769px"></div>

<h2 class="abs section-title" style="left:33px;top:441px">Recent News &amp; Projects</h2>
<article class="abs card" style="left:32px;top:470px"><div class="thumb" role="img" aria-label="Photo of colleagues gathered around a laptop" style="background:linear-gradient(135deg,#d9d3c8,#9aa8b8)"></div><h3>Project-New Tittle</h3><p>Nunc tempus felis vitae urna. Vivamus porttitor, neque at volutpat rutrum, purus nisi eleifend libero</p></article>
<article class="abs card" style="left:216px;top:470px"><div class="thumb" role="img" aria-label="Photo of a business presentation in an office" style="background:linear-gradient(135deg,#6b7078,#c9ced6 60%,#3a3d42)"></div><h3>Project-New Tittle</h3><p>Nunc tempus felis vitae urna. Vivamus porttitor, neque at volutpat rutrum, purus nisi eleifend libero</p></article>
<article class="abs card" style="left:399px;top:470px"><div class="thumb" role="img" aria-label="Photo of a businessman in a blue shirt with arms crossed" style="background:linear-gradient(135deg,#e6eaef,#7fa3cf)"></div><h3>Project-New Tittle</h3><p>Nunc tempus felis vitae urna. Vivamus porttitor, neque at volutpat rutrum, purus nisi eleifend libero</p></article>
<article class="abs card" style="left:583px;top:470px"><div class="thumb" role="img" aria-label="Photo of a smiling woman in a green blouse at a desk" style="background:linear-gradient(135deg,#eceeee,#5f7d52 55%,#d8d8d8)"></div><h3>Project-New Tittle</h3><p>Nunc tempus felis vitae urna. Vivamus porttitor, neque at volutpat rutrum, purus nisi eleifend libero</p></article>

<div class="abs hr" style="left:25px;top:676px;width:510px"></div>
<section class="abs welcome">
  <h2>Welcome to Our Website Main Page</h2>
  <p class="intro">eMira7 is the culmination of a lifelong of challenges that I have overcome personally and professionally in a manner that could inspire or create a dialogue that enables social change. As a person from an ethnic minority who is also an immigrant and is alternatively abled from a mental health diagnosis of Bipolar Affective Disorder I, I have created the project named eMira7.</p>
  <p>As the name the small "e" first represents myself as a person of color who has often had other Australians attempt to make me feel as if I were a second-class citizen. Just recently I had my first experience of racial profiling being stopped on the street for no reason by Coastvale Police. It was amusing rather abusive and I never at any time did I feel unsafe or threatened. Mira is my real first name and the number seven "7" represents someone who owns his disability of Bipolar Disorder. Secondly it represents the nature of the duality of the disorder, and my journey of redemption and self-respect. From a personal standpoint this proposal creates an all-encompassing digital experiment creating groundbreaking opportunities to improve social, health, and economic outcomes of traditionally marginalized visual and non-visual minorities.</p>
</section>

<div class="abs vrule"></div>
<div class="abs side-band" style="left:535px;top:676px;width:212px;height:36px">Watch Latest Video</div>
<div class="abs video" role="img" aria-label="Video still looking up at city skyscrapers against a blue sky">
  <svg class="play" width="38" height="38" viewBox="0 0 38 38"><circle cx="19" cy="19" r="17" fill="none" stroke="#fff" stroke-width="2.5"/><path d="M15 11L27 19 15 27z" fill="#fff"/></svg>
</div>

<div class="abs hr" style="left:25px;top:887px;width:510px"></div>
<section class="abs box" style="left:29px;top:899px">
  <h3>What project would you like to develop?</h3>
  <p>I would like the project to develop and to utilize current Internet, digital technologies and social media to create a template for alternatively abled person's to report the news by themselves and for themselves.</p>
  <p>This would enrich their lives and the lives of others around them, creating a more social sustainable community. eMira7 will create a fully scalable, replicable, and commercially viable model well within the 16-week deadline period. It will be my personal venture into this arena that will demonstrate the model. Once created this model will hopefully stand as a local, state, national, and even international.</p>
  <span class="learn">LEARN MORE</span>
</section>
<section class="abs box" style="left:281px;top:899px">
  <h3>Audience: who would your project impact, assist or reach?</h3>
  <p>The potential audience is very diverse and it has the ability to reach, impact, and assist the global community in ways CivicLane may not have begun to realize. The people who will be impacted are those who are being influenced by decisions of bureaucrats making funding decisions for schools, libraries and communities around Coastvale.</p>
  <p>From the viewpoint of a non-white non-European immigrant the average Australian world-view can unfairly appear to be extremely myopic bordering on parochial, even racist and xenophobic.</p>
  <span class="learn">LEARN MORE</span>
</section>

<div class="abs side-band" style="left:535px;top:886px;width:211px;height:35px">Recent Blog Post</div>
<article class="abs post" style="top:934px"><div class="pic" role="img" aria-label="Portrait photo for blog post" style="background:linear-gradient(135deg,#e5d43a,#4a4a4a)"></div><div><h4>New Tittle goes here</h4><p>Nunc tempus felis vitae urna. Viva-mus porttitor, neque at volutpat</p><a href="#">Learn More</a></div></article>
<article class="abs post" style="top:1000px"><div class="pic" role="img" aria-label="Portrait photo for blog post" style="background:linear-gradient(135deg,#8a6e5e,#2a2a2a)"></div><div><h4>New Tittle goes here</h4><p>Nunc tempus felis vitae urna. Viva-mus porttitor, neque at volutpat</p><a href="#">Learn More</a></div></article>
<article class="abs post" style="top:1073px"><div class="pic" role="img" aria-label="Portrait photo for blog post" style="background:linear-gradient(135deg,#b8a493,#3b2a3a)"></div><div><h4>New Tittle goes here</h4><p>Nunc tempus felis vitae urna. Viva-mus porttitor, neque at volutpat</p><a href="#">Learn More</a></div></article>

<footer class="abs footer">
  <span>Copyright © 1997-2012 Nordel Corporation All Rights Reserved.</span>
  <span>Privacy Policy &nbsp;|&nbsp; Terms of Services</span>
</footer>
</body>
</html>
```